Sol Gorditas Digital Menu Boards

IF SELECTED, WINNER MAY BE HIRED FOR OTHER DESIGNS OF DIFFERENT STORES OF OUR COMPANY.

Task: Digital Menu Boards Design

Task description: We need designs for a Digital Menu to be displayed on two 42’’screens at Solgorditas, a fast-food restaurant in Guadalajara, Mexico. The menu redesign should communicate to our customers the experience of eating at our restaurant.

For avoiding the creation of videos, we are expecting several menu slides with the same text but with different images, simulating the effect of a video where the images are changing. This menu slides will be projected through a USB memory and a slideshow.

Attached files:
For the design, there are several documents attached to the task description:
1. Logo of the restaurant
2. Pictures of the restaurant
3. Example video of what we want to achieve through this menu slides.
4. Pictures of the actual menu board, to be replaced with the new designs.
5. Menu description (regular and breakfast menu)
6. Pictures of each element on the menu (We don’t have yet any breakfast pictures)
**The files are organized on a ZIP file.

Expected product:
For the regular menu,
• 2 menu slide designs for TACOS Y ESPECIALIDADES, where the text will be exactly the same but the images would differ.
• 2 menu slide designs for BEBIDAS Y EXTRAS, where the text will be exactly the same but the images would differ.
For the breakfast menu,
• 1 menu slide including all the menu
Total: 5 menu board slides.

Technical specs:
• You should send the editable file, med and high resolution JPGs for each design.
• The designs should fit perfectly on 42’’ screens.

```html
<!DOCTYPE html>
<html lang="es">
<head>
<meta charset="utf-8">
<title>Sol Gorditas — Desayunos</title>
<link href="https://fonts.googleapis.com/css2?family=Archivo+Black&family=Cuprum:wght@400;700&display=swap" rel="stylesheet">
<style>
  :root {
    --bg: #ffffff;
    --orange: #ff5a00;
    --yellow-a: #f7bb07;
    --yellow-b: #f2b203;
    --yellow-c: #e6a600;
    --row-grey: #e3e3e3;
    --label-grey: #ececec;
    --ink: #111111;
    --green: #3f9a1c;
    --brand-red: #c8102e;
  }
  * { margin: 0; padding: 0; box-sizing: border-box; }
  html, body { width: 1200px; height: 675px; overflow: hidden; background: var(--bg); }
  .board { position: relative; width: 1200px; height: 675px; overflow: hidden; background: var(--bg); font-family: "Cuprum", sans-serif; color: var(--ink); }

  .title-band {
    position: absolute; left: 0; top: 53px; width: 617px; height: 108px;
    background: var(--orange);
    box-shadow: 6px 8px 8px rgba(0,0,0,0.28);
    display: flex; align-items: center; padding-left: 44px;
  }
  .title-band h1 { font-family: "Archivo Black", sans-serif; font-weight: 400; font-size: 42px; color: #fff; letter-spacing: 1px; }

  .menu-table { position: absolute; left: 0; top: 229px; width: 700px; }
  .menu-row { position: absolute; left: 0; width: 700px; background: var(--row-grey); }
  .row-head { top: 0; height: 75px; background: transparent; }
  .row-head .corner { position: absolute; left: 0; top: 0; width: 227px; height: 75px; background: var(--label-grey); }
  .col-head { position: absolute; top: 0; height: 75px; display: flex; align-items: center; justify-content: center; font-size: 27px; }
  .col-pastor { left: 227px; width: 112px; background: var(--yellow-a); }
  .col-arrachera { left: 339px; width: 158px; background: var(--yellow-a); }
  .col-queso { left: 497px; width: 95px; background: var(--yellow-b); }
  .col-huevo { left: 592px; width: 101px; background: var(--yellow-c); }

  .row-chilaquiles { top: 78px; height: 69px; }
  .row-burritos { top: 150px; height: 74px; }
  .row-tacos { top: 230px; height: 141px; }

  .dish { position: absolute; left: 25px; font-size: 26px; letter-spacing: 1.5px; line-height: 1.25; }
  .price { position: absolute; font-size: 26px; letter-spacing: 1px; }

  .photo-side { position: absolute; inset: 0; pointer-events: none; }

  .brand { position: absolute; left: 880px; top: 78px; display: flex; align-items: center; gap: 12px; }
  .brand-dot { width: 26px; height: 26px; border-radius: 50%; background: var(--brand-red); }
  .brand-name { font-family: "Cuprum", sans-serif; font-weight: 700; font-size: 46px; color: var(--brand-red); }
</style>
</head>
<body>
<main class="board">
  <svg class="photo-side" width="1200" height="675" viewBox="0 0 1200 675">
    <defs>
      <linearGradient id="tacoTones" x1="0" y1="0" x2="1" y2="1">
        <stop offset="0" stop-color="#eef0e6"/>
        <stop offset="0.35" stop-color="#e8d7b4"/>
        <stop offset="0.65" stop-color="#c9673a"/>
        <stop offset="1" stop-color="#e9dcc0"/>
      </linearGradient>
    </defs>
    <path role="img" aria-label="Fotografía de tacos al pastor con piña, cebolla y cilantro"
          d="M 793 0 Q 660 300 705 675 L 1200 675 L 1200 0 Z" fill="url(#tacoTones)"/>
    <path d="M 793 0 Q 660 300 705 675" fill="none" stroke="var(--green)" stroke-width="9"/>
  </svg>

  <div class="brand">
    <span class="brand-dot"></span>
    <span class="brand-name">Sol Gorditas</span>
  </div>

  <header class="title-band"><h1>DESAYUNOS</h1></header>

  <section class="menu-table">
    <div class="menu-row row-head">
      <div class="corner"></div>
      <div class="col-head col-pastor">PASTOR</div>
      <div class="col-head col-arrachera">ARRACHERA</div>
      <div class="col-head col-queso">QUESO</div>
      <div class="col-head col-huevo">HUEVO</div>
    </div>

    <div class="menu-row row-chilaquiles">
      <span class="dish" style="top:16px">CHILAQUILES</span>
      <span class="price" style="left:248px;top:18px">45$</span>
      <span class="price" style="left:381px;top:22px">45$</span>
    </div>

    <div class="menu-row row-burritos">
      <span class="dish" style="top:18px">BURRITOS</span>
      <span class="price" style="left:244px;top:18px">45$</span>
      <span class="price" style="left:378px;top:24px">45$</span>
      <span class="price" style="left:505px;top:18px">45$</span>
      <span class="price" style="left:603px;top:20px">45$</span>
    </div>

    <div class="menu-row row-tacos">
      <span class="dish" style="top:10px">TACOS<br>DORADOS(3)</span>
      <span class="price" style="left:244px;top:12px">40$</span>
      <span class="price" style="left:378px;top:16px">40$</span>
    </div>
  </section>
</main>
</body>
</html>
```